New cake shop needs a gorgeous website!

I need an easy to navigate and update (from my Mac - in layman's terms!) website for my new business - Crumb & Fern. This is a dietary friendly cake shop in Ponsonby, Auckland, New Zealand. We will be having Tarawhiti coffee (organic, fair-trade) Lumen Fizz range and specialty teas. Eat in, takeaway and delivery.
I will require you to upload and write if necessary, onto a program such as Pagecraft or similar.
I need a homepage, gallery page, price and ordering page (although the orders will be done via email/phone, no payments will be taken directly from the website) about us page, products and services page(this could incorporate the gallery maybe) a classes info page and a contact page.
My branding is very modern and clean. No vintage or french industrial is to be seen! We are sleek, with lots of white, black, charcoal grey and hot pink.
I will have photos to use in about 10 days, but I will upload some temporary images to start you off....
We also have a focus on 'a little bit good for you' and aim to make cakes that everyone can eat, whether they be gluten, dairy or egg intolerant or trying to lower the sugar in their diet.
A great design will be modern, exciting and convey a feel of luxury.
Please check out my pinterest page http://www.pinboardly.example/wrenbolt/coffee-cards-flyers-and-websites/
and feel free to use images from my instagram - fernbakenz.
Thanks!

```html
<!DOCTYPE html>
<html lang="en">
<head>
<meta charset="utf-8">
<title>Crumb &amp; Fern</title>
<link href="https://fonts.googleapis.com/css2?family=Montserrat:wght@400;600;700&family=Great+Vibes&display=swap" rel="stylesheet">
<style>
:root{
  --pink:#e04a7f;
  --black:#111111;
  --charcoal:#2a2a2a;
  --grey:#6b6b6b;
  --light:#f4f4f4;
  --white:#ffffff;
  --coffee-dark:#2c1b14;
  --cola-dark:#3a1216;
}
*{margin:0;padding:0;box-sizing:border-box}
html,body{width:1200px;height:2552px;overflow:hidden;background:var(--white);font-family:'Montserrat',sans-serif;color:var(--charcoal)}
.page{width:1200px;height:2552px;position:relative}

.site-header{height:88px;display:flex;align-items:center;justify-content:space-between;padding:0 150px}
.brand{font-size:40px;font-weight:700;color:var(--pink);letter-spacing:1px}
.search{display:flex;align-items:center;gap:10px;font-size:13px;color:var(--grey);border-bottom:1px solid #ccc;padding:4px 0;width:210px}
.main-nav{height:40px;border-top:1px solid #ddd;border-bottom:1px solid #ddd;display:flex;justify-content:space-between;align-items:center;padding:0 150px}
.main-nav a{font-size:13px;font-weight:600;color:var(--black);text-decoration:none;letter-spacing:1px}
.main-nav span{width:1px;height:18px;background:#ccc}

.hero{position:relative;height:552px;background:radial-gradient(ellipse at 50% 55%,#8a4a32 0%,#5c3122 45%,#2e1a14 100%)}
.hero-title{position:absolute;top:230px;width:100%;text-align:center;color:var(--white);font-size:46px;font-weight:400;line-height:1.25;text-shadow:0 2px 8px rgba(0,0,0,.4)}
.hero-arrow{position:absolute;top:250px}
.hero-arrow.left{left:90px}.hero-arrow.right{right:90px}
.hero-dots{position:absolute;bottom:22px;width:100%;display:flex;justify-content:center;gap:10px}
.hero-dots i{width:14px;height:14px;border:2px solid var(--white);border-radius:50%}
.hero-dots i.on{background:var(--white)}

.welcome{height:380px;background:var(--charcoal);display:flex;align-items:center;padding:0 150px;gap:60px}
.welcome-photo{width:340px;height:280px;background:linear-gradient(135deg,#e6e2de 0%,#8a5e44 55%,#3a2116 100%)}
.welcome-copy{flex:1;color:var(--white)}
.welcome-copy h2{font-size:40px;font-weight:700;letter-spacing:1px}
.welcome-copy h3{font-size:18px;font-weight:600;letter-spacing:2px;margin-bottom:18px}
.welcome-copy p{font-size:14px;line-height:1.6;color:#d8d8d8;margin-bottom:12px}
.phone{display:flex;align-items:center;gap:16px;font-size:26px;margin-top:16px}

.dietary{height:380px;display:flex;align-items:center;padding:0 150px;gap:50px}
.dietary-copy{width:360px;text-align:center}
.script{font-family:'Great Vibes',cursive;color:var(--pink);font-size:64px;line-height:1}
.kicker{font-size:20px;font-weight:600;letter-spacing:3px;margin:4px 0 18px}
.body-text{font-size:13px;line-height:1.7;text-transform:uppercase}
.read-more{display:inline-flex;align-items:center;gap:10px;font-size:13px;font-weight:600;margin-top:14px}
.cake-grid{flex:1;display:grid;grid-template-columns:1fr 1fr;gap:14px}
.cake-grid div{height:158px}
.cake-1{background:linear-gradient(160deg,#f2d5d8,#c41f3b)}
.cake-2{background:linear-gradient(160deg,#6a3320,#2a130b)}
.cake-3{background:linear-gradient(160deg,#8a2a3a,#3b1a12)}
.cake-4{background:linear-gradient(160deg,#5a2a1a,#c23a4a)}

.coffee{height:380px;background:linear-gradient(90deg,#3a2419,var(--coffee-dark) 60%,#4a2e20);display:flex;align-items:center;padding:0 150px 0 190px;gap:70px}
.coffee-photo{width:340px;height:240px;background:linear-gradient(135deg,#5c3a22 0%,#b8814c 50%,#2a1a12 100%)}
.coffee-copy{flex:1;text-align:center;color:var(--white)}
.coffee-copy .kicker{color:var(--white)}

.cola{height:300px;background:linear-gradient(90deg,#2a0c10,var(--cola-dark) 50%,#5a161c);display:flex;flex-direction:column;align-items:center;justify-content:center;color:var(--white);text-align:center;padding:0 260px}
.cola-label{border:2px solid var(--white);padding:8px 34px;font-size:20px;font-weight:600;letter-spacing:3px;margin-bottom:20px}

.contact{height:320px;display:flex;align-items:center;padding:0 150px;gap:60px}
.map{width:450px;height:240px;background:linear-gradient(135deg,#dfe6d8,#c9d5e0)}
.contact-copy{flex:1;text-align:center}
.contact-copy p{font-size:12px;line-height:1.8;text-transform:uppercase;white-space:nowrap}

.site-footer{height:112px;background:var(--black);color:var(--white);display:flex;justify-content:space-between;align-items:center;padding:0 150px;font-size:12px}
.social{display:flex;gap:8px;margin-top:10px}
.social i{width:22px;height:22px;background:var(--grey)}
.foot-nav{text-align:right;line-height:2}
.foot-nav span{letter-spacing:1px}
</style>
</head>
<body>
<div class="page">
  <header class="site-header">
    <div class="brand">CRUMB &amp; FERN</div>
    <div class="search">
      <svg width="16" height="16" viewBox="0 0 16 16"><circle cx="6.5" cy="6.5" r="5" fill="none" stroke="#666" stroke-width="2"/><line x1="10" y1="10" x2="15" y2="15" stroke="#666" stroke-width="2"/></svg>
      SEARCH
    </div>
  </header>
  <nav class="main-nav">
    <a>HOME</a><span></span><a>ABOUT</a><span></span><a>COFFEE</a><span></span><a>COLA</a><span></span><a>SERVICES</a><span></span><a>BLOG</a><span></span><a>LATEST</a><span></span><a>CONTACT</a>
  </nav>

  <section class="hero" role="img" aria-label="Close-up of a cake topped with yellow flowers and berries">
    <h1 class="hero-title">organic coffee and<br>cola at our stores</h1>
    <svg class="hero-arrow left" width="24" height="40" viewBox="0 0 24 40"><polyline points="20,4 4,20 20,36" fill="none" stroke="#fff" stroke-width="5"/></svg>
    <svg class="hero-arrow right" width="24" height="40" viewBox="0 0 24 40"><polyline points="4,4 20,20 4,36" fill="none" stroke="#fff" stroke-width="5"/></svg>
    <div class="hero-dots"><i class="on"></i><i></i><i></i><i></i></div>
  </section>

  <section class="welcome">
    <div class="welcome-photo" role="img" aria-label="White cup filled with roasted coffee beans"></div>
    <div class="welcome-copy">
      <h2>WELCOME</h2>
      <h3>TO OUR SITE</h3>
      <p>Crumb &amp; Fern bakes cakes that everyone can share, whether you avoid gluten, dairy or egg, or simply want less sugar. Every slice is made by hand in our Ponsonby kitchen each morning.</p>
      <p>Pull up a stool for an organic coffee, pick a cake to take home, or ask us to deliver a whole one to your door.</p>
      <div class="phone">
        <svg width="40" height="40" viewBox="0 0 40 40"><circle cx="20" cy="20" r="19" fill="none" stroke="#fff" stroke-width="2"/><path d="M13 12c2-2 4 0 5 2s-1 3-1 4 3 5 5 5 2-2 4-1 4 3 1 5-13-4-14-15z" fill="#fff"/></svg>
        414.XXX.XXXX
      </div>
    </div>
  </section>

  <section class="dietary">
    <div class="dietary-copy">
      <div class="script">Dietary</div>
      <div class="kicker">FRIENDLY CAKE</div>
      <p class="body-text">Gluten free, dairy free and egg free cakes baked fresh every day with natural sweeteners, whole ingredients and plenty of care, so nobody at the table misses out on dessert.</p>
      <div class="read-more">READ MORE <svg width="22" height="10" viewBox="0 0 22 10"><path d="M0 5h20M16 1l4 4-4 4" fill="none" stroke="#e04a7f" stroke-width="2"/></svg></div>
    </div>
    <div class="cake-grid">
      <div class="cake-1" role="img" aria-label="Cheesecake topped with red berry glaze"></div>
      <div class="cake-2" role="img" aria-label="Slice of chocolate layer cake"></div>
      <div class="cake-3" role="img" aria-label="Chocolate cake topped with mixed berries"></div>
      <div class="cake-4" role="img" aria-label="Chocolate cake with strawberries on top"></div>
    </div>
  </section>

  <section class="coffee" role="img" aria-label="Coffee beans spread across a dark background">
    <div class="coffee-photo" role="img" aria-label="Latte with leaf pattern in the foam"></div>
    <div class="coffee-copy">
      <div class="script">Organic</div>
      <div class="kicker">COFFEE</div>
      <p class="body-text">Fair trade organic beans roasted in small batches and poured by our baristas, the perfect partner for a slice of cake at any hour of the day.</p>
      <div class="read-more">READ MORE <svg width="22" height="10" viewBox="0 0 22 10"><path d="M0 5h20M16 1l4 4-4 4" fill="none" stroke="#e04a7f" stroke-width="2"/></svg></div>
    </div>
  </section>

  <section class="cola" role="img" aria-label="Chilled cola bottles in soft red light">
    <div class="cola-label">COLA</div>
    <p class="body-text">A sparkling organic cola range made with real cane sugar and natural botanicals, served ice cold in store or packed for takeaway with your cake order.</p>
    <div class="read-more">READ MORE <svg width="22" height="10" viewBox="0 0 22 10"><path d="M0 5h20M16 1l4 4-4 4" fill="none" stroke="#fff" stroke-width="2"/></svg></div>
  </section>

  <section class="contact">
    <div class="map" role="img" aria-label="Map showing the shop location"></div>
    <div class="contact-copy">
      <div class="script">Contact</div>
      <div class="kicker">STAY WITH US</div>
      <p>Street Address 1 | Street Address 2<br>City, State, Pincode<br>P: 414.XXX.XXXX<br>E: hello@crumbandfern.example</p>
    </div>
  </section>

  <footer class="site-footer">
    <div>
      FOLLOW US ON
      <div class="social"><i></i><i></i><i></i><i></i></div>
    </div>
    <div class="foot-nav">
      <span>HOME | ABOUT US | COFFEE | COLA | NEWS | SERVICES | BLOG | CONTACT</span><br>
      <span>COPYRIGHT © 2014 ALL RIGHTS RESERVED</span>
    </div>
  </footer>
</div>
</body>
</html>
```